VerdaTurfix - 11" x 4" Door Hanger, full color both sides

We need a door hanger designed, 11" x 4", full color both sides, We are a lawn care company that provides lawn mowing, and other services to clients. This door hanger will be place on the 9 neighbors of our current clients. The ad needs to state that we provided lawn service to one of their neighbors today, and that we are in their neighborhood each week on that day. The door hanger will have 4 printings, substituting the day of Tuesday, Wednesday, Thursday, and Friday. All the art work and text will remain the same except the day of the week. For information about VerdaTurfix, please visit our website www.verdaturfix.net. The main emphasis of the message should be that we are their every week on that day, and the benefits to them of using our service (ie. quality time with their family, golf, sports, resting, etc., instead of mowing the lawn). At the bottom of the door hanger will be a coupon offering their tenth (10th) lawn service free, which is the same as a 10% discount.

I have uploaded a template files for the front and back of an 11 x 4 door hanger, The templates are pdf, jpeg, or eps files. The final product can be a pdf, jpeg, or eps file.

Target Market(s)

Neighbors of our existing clients

Industry/Entity Type

Lawn Care

Font styles to use
Serif

Requirements
Must have
• Professional design and art, Short conversational message that relays the following thoughts:
• 1. We mowed your neighbor's lawn today!
• 2. We are in your neighborhood every Tuesday!
• 3. Our lawn service is guaranteed.
• 4. Call to action - Call us today! 555-014-7382
• 5. Of course our contact info, name, phone number, website address.
• 6. Coupon at bottom for "10th lawn service Free!"
Nice to have
• Art work from our website is fine to use, That carries our theme throughout our campaign.
Should not have
• Very wordy. This is basically a billboard, Have very few seconds to grab their attention.

```html
<!DOCTYPE html>
<html lang="en">
<head>
<meta charset="utf-8">
<title>VerdaTurfix Door Hanger</title>
<link rel="stylesheet" href="https://fonts.googleapis.com/css2?family=Oswald:wght@300;400;500&family=Raleway:wght@400;500;600&display=swap">
<style>
  :root {
    --page-bg: #ebebeb;
    --white: #ffffff;
    --charcoal: #333333;
    --leaf: #8dc63f;
    --forest: #0d7a3c;
    --turf-deep: #2c5a1e;
    --coupon: #9a8fca;
    --coupon-ring: #5ec7cf;
    --text-soft: #d8d8d8;
    --ink: #1f2a14;
  }
  * { margin: 0; padding: 0; box-sizing: border-box; }
  html, body { width: 1200px; height: 1200px; overflow: hidden; background: var(--page-bg); }
  .sheet { position: relative; width: 1200px; height: 1200px; }
  .hanger {
    position: absolute; top: 26px; width: 449px; height: 1147px;
    background: var(--white); overflow: hidden;
    box-shadow: 0 2px 6px rgba(0,0,0,0.18);
  }
  .hanger--front { left: 100px; }
  .hanger--back { left: 652px; }
  .hanger__art { position: absolute; inset: 0; width: 449px; height: 1147px; }
  .brand {
    position: absolute; left: 19px; top: 14px;
    font-family: "Oswald", sans-serif; font-weight: 500; font-size: 30px;
    color: #111; letter-spacing: 0.2px;
  }
  .headline {
    position: absolute; left: 22px; top: 590px; width: 284px;
    font-family: "Oswald", sans-serif; font-weight: 300; color: var(--white);
    text-transform: uppercase; line-height: 1;
  }
  .headline__lead { display: block; font-size: 25px; padding-left: 18px; }
  .headline__main { display: block; font-size: 58px; margin-top: 2px; letter-spacing: -0.5px; }
  .headline__tail { display: block; font-size: 25px; text-align: right; margin-top: 2px; }
  .message {
    position: absolute; left: 23px; top: 738px;
    font-family: "Raleway", sans-serif; font-weight: 400; font-size: 27px;
    line-height: 37.5px; color: var(--white); text-transform: uppercase; white-space: nowrap;
  }
  .coupon {
    position: absolute; left: 258px; top: 936px; width: 164px; height: 164px;
    border-radius: 50%; background: var(--coupon);
    display: flex; flex-direction: column; align-items: center; justify-content: center;
    font-family: "Oswald", sans-serif; font-weight: 400; color: var(--white); text-transform: uppercase;
    text-align: center; line-height: 1;
  }
  .coupon::after {
    content: ""; position: absolute; inset: 6px; border-radius: 50%;
    border: 2px solid var(--coupon-ring);
  }
  .coupon__big { font-size: 32px; text-transform: none; margin-bottom: 4px; }
  .coupon__small { font-size: 23px; line-height: 1.05; }
  .coupon-tag { position: absolute; left: 244px; top: 902px; width: 64px; height: 64px; }
  .about {
    position: absolute; left: 23px; top: 558px; width: 286px;
    font-family: "Raleway", sans-serif; color: var(--text-soft);
  }
  .about__title {
    font-family: "Oswald", sans-serif; font-weight: 400; font-size: 37px;
    color: var(--leaf); line-height: 1; margin-bottom: 8px;
  }
  .about__text {
    font-size: 14px; line-height: 17px; text-align: justify; margin-bottom: 17px;
    hyphens: auto; -webkit-hyphens: auto;
  }
  .services {
    position: absolute; left: 22px; top: 848px; width: 420px;
    font-family: "Raleway", sans-serif; color: var(--ink);
  }
  .services__title {
    font-family: "Oswald", sans-serif; font-weight: 400; font-size: 20px; line-height: 1; margin-bottom: 4px;
  }
  .services__list { list-style: none; font-size: 12.2px; font-weight: 600; line-height: 16.8px; }
  .services__list li::before { content: "\25AA"; margin-right: 4px; }
  .services__list .sub { padding-left: 10px; }
  .contact {
    position: absolute; left: 0; top: 1073px; width: 449px; text-align: center;
    font-family: "Raleway", sans-serif; color: var(--text-soft); font-size: 15px; line-height: 20.5px;
  }
  .contact__name { font-weight: 600; font-size: 17px; color: var(--white); }
</style>
</head>
<body>
<div class="sheet">

  <section class="hanger hanger--front">
    <svg class="hanger__art" viewBox="0 0 374 956" preserveAspectRatio="none">
      <defs>
        <linearGradient id="mowGrass" x1="0" y1="0" x2="0.4" y2="1">
          <stop offset="0" stop-color="#4d7a2a"/>
          <stop offset="0.55" stop-color="#3f7024"/>
          <stop offset="1" stop-color="#2c5a1e"/>
        </linearGradient>
      </defs>
      <polygon role="img" aria-label="Photo of a red lawn mower cutting green grass" points="287,0 374,0 374,520 0,322 0,170" fill="url(#mowGrass)"/>
      <polygon points="0,345 374,545 374,956 0,956" fill="var(--charcoal)"/>
      <polygon points="0,78 77,120 0,163" fill="var(--leaf)"/>
      <polygon points="18,160 77,120 77,193" fill="var(--forest)"/>
      <polygon points="277,483 374,537 277,593" fill="var(--forest)"/>
      <polygon points="374,537 374,645 277,593" fill="var(--leaf)"/>
      <circle cx="179" cy="104" r="56" fill="none" stroke="#3fb4e0" stroke-width="1" stroke-dasharray="4 3"/>
      <circle cx="179" cy="104" r="49" fill="none" stroke="#222" stroke-width="1" stroke-dasharray="4 3"/>
      <line x1="228" y1="104" x2="374" y2="104" stroke="#222" stroke-width="1" stroke-dasharray="4 3"/>
    </svg>
    <div class="brand">VERDATURFIX</div>
    <h1 class="headline">
      <span class="headline__lead">We are their</span>
      <span class="headline__main">Every Week</span>
      <span class="headline__tail">On that day</span>
    </h1>
    <p class="message">We provided lawn<br>service to one<br>of their neighbors<br>today, and that<br>we are in their<br>neighborhood<br>each week<br>on that day.</p>
    <div class="coupon">
      <span class="coupon__big">10th</span>
      <span class="coupon__small">Lawn<br>Service<br>Free</span>
    </div>
    <svg class="coupon-tag" viewBox="0 0 70 70" aria-hidden="true">
      <path d="M8 6 C2 14 6 24 16 22" fill="none" stroke="var(--coupon-ring)" stroke-width="2"/>
      <polygon points="18,18 34,14 46,30 36,40 20,32" fill="var(--coupon-ring)"/>
      <circle cx="24" cy="22" r="2.5" fill="var(--white)"/>
    </svg>
  </section>

  <section class="hanger hanger--back">
    <svg class="hanger__art" viewBox="0 0 374 956" preserveAspectRatio="none">
      <defs>
        <linearGradient id="handGrass" x1="0" y1="0" x2="0" y2="1">
          <stop offset="0" stop-color="#1f5a2a"/>
          <stop offset="0.5" stop-color="#2f6f2a"/>
          <stop offset="1" stop-color="#3f8030"/>
        </linearGradient>
      </defs>
      <polygon role="img" aria-label="Photo of a hand resting on a freshly cut lawn" points="287,0 374,0 374,530 0,322 0,170" fill="url(#handGrass)"/>
      <polygon points="0,343 374,550 374,690 0,690" fill="var(--charcoal)"/>
      <rect x="0" y="690" width="374" height="200" fill="var(--leaf)"/>
      <rect x="0" y="890" width="374" height="66" fill="var(--charcoal)"/>
      <polygon points="0,78 77,120 0,163" fill="var(--leaf)"/>
      <polygon points="18,160 77,120 77,193" fill="var(--forest)"/>
      <polygon points="277,483 374,537 277,593" fill="var(--forest)"/>
      <polygon points="374,537 374,645 277,593" fill="var(--leaf)"/>
      <circle cx="157" cy="104" r="56" fill="none" stroke="#3fb4e0" stroke-width="1" stroke-dasharray="4 3"/>
      <circle cx="157" cy="104" r="49" fill="none" stroke="#222" stroke-width="1" stroke-dasharray="4 3"/>
      <line x1="206" y1="104" x2="374" y2="104" stroke="#222" stroke-width="1" stroke-dasharray="4 3"/>
    </svg>
    <div class="brand">VERDATURFIX</div>
    <div class="about">
      <h2 class="about__title">About Us</h2>
      <p class="about__text">VerdaTurfix is a family owned company. VerdaTurfix's mission is to bring service excellence to our client. Our goal is to provide this service excellence in our administrative areas, as well as in the field operations.</p>
      <p class="about__text">By providing our clients guaranteed service excellence, they are able to spend quality time with their family, rather than doing lawn work.</p>
    </div>
    <div class="services">
      <h3 class="services__title">SERVICES:</h3>
      <ul class="services__list">
        <li>Weekly and bi-weekly lawn care service,</li>
        <li>Fertilization and weed control services,</li>
        <li>Lawn insect, grub worm, and fire ant control,</li>
        <li>Sprinkler repair, and irrigation modification</li>
        <li>Other landscape services, including but not limited to:</li>
        <li class="sub">Planting plants and trees,</li>
        <li class="sub">Seasonal flowers,</li>
        <li class="sub">Trimming of plants and hedges,</li>
        <li class="sub">Providing and installing mulch</li>
        <li class="sub">Providing and installing stone or metal planting bed borders.</li>
        <li class="sub">Additional services.</li>
      </ul>
    </div>
    <div class="contact">
      <div><span class="contact__name">VerdaTurfix</span> | P. O. Box 1208 Cedarbrook, TX 75099</div>
      <div>Tel 555.014.7382 | Fax 555.014.7390</div>
      <div>Email: service@verdaturfix.net | www.verdaturfix.net</div>
    </div>
  </section>

</div>
</body>
</html>
```